Multiple website banners for a shopify theme

I need custom designed banners for a destributor webpage.

We will be selling products in our local store from a supplier https://pipwellsoaps.co.uk (you can get the ideas from their site).

We need custom desings:
- 2-3x 1920x745
- 1x 960x960
- 2x 480x480
- 1x 960*480
All of theme need to nicely fit together as shown in the uploaded layout screenshot (website_banner_layout).
In Google drive link there are products pictures which must be used in the banners.

https://files.mornavex.com/share/folders/8QpTzK2wLmVa7HnYcRbE5dUsXoGi3JfKt?usp=sharing

Target Market(s)

Kids, Cosmetics market

Industry/Entity Type

Cosmetics

Requirements
Must have
• Playful elements

```html
<!DOCTYPE html>
<html lang="en">
<head>
<meta charset="utf-8">
<title>Pipwell Kozmetika – Fizzers banner</title>
<link href="https://fonts.googleapis.com/css2?family=Fredoka:wght@700&family=Questrial&display=swap" rel="stylesheet">
<style>
  :root {
    --bg-pink: #f7c9dd;
    --hot-pink: #ec4a9a;
    --bubble-pink: #f066a9;
    --aqua: #7fd3e0;
    --white: #ffffff;
    --bomb-cream: #f6e7e4;
    --bomb-sky: #8ed3ee;
    --bomb-rose: #f3a6c8;
    --glaze-blue: #3ab7d4;
  }
  html, body {
    margin: 0;
    padding: 0;
    overflow: hidden;
  }
  .banner {
    position: relative;
    width: 1200px;
    height: 466px;
    background: var(--bg-pink);
    overflow: hidden;
    font-family: "Questrial", sans-serif;
  }
  .brand {
    position: absolute;
    left: 66px;
    top: 40px;
    display: flex;
    align-items: center;
    gap: 12px;
  }
  .brand-dot {
    width: 46px;
    height: 46px;
    border-radius: 50%;
    background: var(--hot-pink);
  }
  .brand-name {
    font-family: "Fredoka", sans-serif;
    font-weight: 700;
    font-size: 26px;
    line-height: 1.05;
    letter-spacing: 1px;
    color: var(--hot-pink);
    text-transform: uppercase;
  }
  .headline {
    position: absolute;
    left: 66px;
    top: 140px;
    margin: 0;
    font-family: "Fredoka", sans-serif;
    font-weight: 700;
    font-size: 118px;
    line-height: 1;
    letter-spacing: 1px;
    color: var(--aqua);
    -webkit-text-stroke: 10px var(--white);
    paint-order: stroke fill;
  }
  .tagline {
    position: absolute;
    left: 68px;
    top: 262px;
    margin: 0;
    font-size: 49px;
    line-height: 57px;
    color: var(--white);
  }
  .product-stage {
    position: absolute;
    left: 0;
    top: 0;
    width: 1200px;
    height: 466px;
  }
</style>
</head>
<body>
  <main class="banner">
    <div class="brand">
      <span class="brand-dot"></span>
      <span class="brand-name">Pipwell<br>Kozmetika</span>
    </div>

    <h1 class="headline">Fizzers!</h1>
    <p class="tagline">Bathtime has<br>never been so<br>sweet!</p>

    <svg class="product-stage" viewBox="0 0 1200 466" aria-hidden="false">
      <defs>
        <radialGradient id="bomb-cream-glaze" cx="50%" cy="35%" r="65%">
          <stop offset="0%" stop-color="var(--glaze-blue)"/>
          <stop offset="55%" stop-color="var(--bomb-cream)"/>
          <stop offset="100%" stop-color="var(--bomb-rose)"/>
        </radialGradient>
        <radialGradient id="bomb-sky-swirl" cx="50%" cy="35%" r="65%">
          <stop offset="0%" stop-color="var(--white)"/>
          <stop offset="50%" stop-color="#b9def4"/>
          <stop offset="100%" stop-color="var(--bomb-sky)"/>
        </radialGradient>
        <radialGradient id="bomb-rose-swirl" cx="50%" cy="30%" r="65%">
          <stop offset="0%" stop-color="#fff6e2"/>
          <stop offset="45%" stop-color="#5b8fe0"/>
          <stop offset="100%" stop-color="var(--bomb-rose)"/>
        </radialGradient>
      </defs>
      <circle class="feature-circle" cx="950" cy="394" r="349" fill="var(--hot-pink)"/>
      <circle cx="899" cy="200" r="112" fill="url(#bomb-sky-swirl)" role="img" aria-label="Sky blue bath bomb topped with white whipped swirl and a blue gem"/>
      <circle cx="1058" cy="356" r="140" fill="url(#bomb-rose-swirl)" role="img" aria-label="Pink bath bomb with blue drip, cream swirl, sprinkles and an ice lolly topper"/>
      <circle cx="783" cy="390" r="122" fill="url(#bomb-cream-glaze)" role="img" aria-label="Cream and pink bath bomb with aqua glaze drip, red cherry and pink sprinkles"/>
    </svg>
  </main>
</body>
</html>
```